Business Card for a Candle Company. - Creative Hipster Styling :)

I am after a two sided Business Card. Contact information on the front, text that will be supplied (and details further on here) on the back. Ideally I am looking for someone I can continue to work with in the future for flyers, labels, marketing material etc.

I have a Logo which I am using as the labels for the candle and have attached all the versions of the file I was given. I am after a similar feel to my logo and love the font and the feather used. it is important that my card looks like it is meant to go with the logo.

I would love you to use your imagination and see what can be thought up :)

All my candles are either clear or black glass and packaging is black and labels are white, on a square label with black writing (see attachments)

I love the feather on the logo if it can be incorporated great, if the business card looks better without it than that is fine too..

Target Market(s)

I am a new candle company and the feel I'm going for is a little luxury a little hipster. Imagine the candle going into a converted warehouse studio in the city.

Industry/Entity Type

Home And Garden

Contact Information for Business Card

I have a Logo which I am using as the labels for the candle and have attached all the versions of the file I was given. I am after a similar feel to my logo and love the font used but its caps and I don't really want everything in CAPS. It is important thought that everything goes together.

I love the feather on the logo if it can be incorporated great, if the business card looks better without it than that is fine too.

Norrel Glow Co
Marrow Coast, KS Australia
A little wax company, in a garage, on the coast.
craftmarketa.com/au/shop/NorrelGlowCo
sociallinka.com.au/norrelglowco
norrelglowco@mailbrook.com.au
Jess Pendell
0481 276 152.

On the back of the card I need it to look good and go with the design on the front but want a bit of text;

To give you an idea of what I want on the back I've put what I've got following but I'm still working on grammar and wording so it may change slightly before the final edit.

We would love to see how you display your candle or reuse the glass vessel and would love to see a photo!
Check out ideas and share yours on your social media #norrelglowco

Just a few ideas to reuse your vessel;

A Vase to Display fresh flowers
Lolly Jar for your favourite candy
Decorate with baubles at Christmas
Bathroom Vanity Storage
Decorate with eggs at Easter
Plant a teranium inside.

Font styles to use
Decorative
Script
Other font styles liked:
• OctinVintageFree

Colors
000000
ffffff
757575

Requirements
Must have
• The only must is that it needs to look like it goes with my logo which I am using as the labels on the actual candle. the labels are white with black details and are square.
• Not too structured if possible as it is a creative company rather that a professional services company.
• I want people to pick up the card and think it looks great. I believe a business card is a very useful marketing tool and should be used as such. One card will be included in with each candle so that customers can re order.
Nice to have
• I love the feather on the logo if it can be incorporated great, if the business card looks better without it than that is fine too.
• Card just needs to fit with the logo.
Should not have
• It should not be a boring card. :)

```html
<!DOCTYPE html>
<html lang="en">
<head>
<meta charset="utf-8">
<title>Norrel Glow Co – Business Card</title>
<link rel="stylesheet" href="https://fonts.googleapis.com/css2?family=Courier+Prime:wght@400;700&family=Damion&family=Source+Sans+3:wght@400&family=Source+Serif+4:wght@400;700&display=swap">
<style>
  :root {
    --stage: #d1d2d4;
    --ink: #231f20;
    --card-dark: #231f20;
    --paper-light: #ffffff;
    --paper-edge: #b9babc;
    --feather-tone: #6b5a55;
    --white: #ffffff;
    --label: #1a1a1a;
  }
  * { box-sizing: border-box; margin: 0; padding: 0; }
  html, body { width: 1200px; height: 440px; overflow: hidden; }
  body {
    background: var(--stage);
    position: relative;
    font-family: "Source Sans 3", Arial, sans-serif;
  }
  .side-label {
    position: absolute;
    font-size: 22px;
    color: var(--label);
    letter-spacing: 0.5px;
  }
  .side-label--front { left: 79px; top: 43px; }
  .side-label--back { left: 617px; top: 49px; }

  .card {
    position: absolute;
    width: 506px;
    height: 304px;
  }

  /* Front */
  .card--front {
    left: 80px;
    top: 87px;
    background: radial-gradient(ellipse 60% 65% at 50% 50%, var(--paper-light) 0%, #ececed 45%, var(--paper-edge) 100%);
    color: var(--ink);
    text-align: center;
  }
  .front__est {
    position: absolute; left: 0; right: 0; top: 51px;
    font-family: "Courier Prime", "Courier New", monospace;
    font-size: 12px;
    letter-spacing: 2px;
  }
  .front__brand {
    position: absolute; left: 0; right: 0; top: 80px;
    font-family: "Courier Prime", "Courier New", monospace;
    font-size: 30px;
    letter-spacing: 3px;
  }
  .front__feather {
    position: absolute; left: 169px; top: 138px;
    width: 184px; height: 48px;
    border-radius: 50%;
    background: radial-gradient(ellipse at 55% 50%, rgba(107,90,85,0.55) 0%, rgba(107,90,85,0.25) 55%, rgba(107,90,85,0) 75%);
  }
  .front__tagline {
    position: absolute; left: 0; right: 0; top: 195px;
    font-family: "Damion", cursive;
    font-size: 21px;
  }
  .front__region {
    position: absolute; left: 0; right: 0; top: 227px;
    font-size: 12px;
    letter-spacing: 3px;
  }

  /* Back */
  .card--back {
    left: 617px;
    top: 86px;
    background: var(--card-dark);
    color: var(--white);
  }
  .back__name {
    position: absolute; left: 0; right: 0; top: 38px;
    text-align: center;
    font-family: "Damion", cursive;
    font-size: 40px;
    padding-left: 6px;
  }
  .contact {
    position: absolute;
    display: flex;
    align-items: center;
    gap: 10px;
    font-size: 11.5px;
  }
  .contact svg { width: 18px; height: 18px; flex: none; fill: var(--white); }
  .contact--location { left: 64px; top: 121px; }
  .contact--phone { left: 64px; top: 157px; }
  .contact--email { left: 272px; top: 121px; }
  .contact--web { left: 272px; top: 157px; font-size: 10.5px; }

  .back__invite {
    position: absolute; left: 70px; top: 230px;
    width: 365px; height: 29px;
    border: 1px solid var(--white);
    text-align: center;
    font-family: "Source Serif 4", "Times New Roman", serif;
    font-size: 7.3px;
    line-height: 1.3;
    padding-top: 4px;
    color: var(--white);
  }
  .back__invite strong { font-size: 9px; }
  .back__ideas {
    position: absolute; left: 0; right: 0; top: 266px;
    text-align: center;
    font-family: "Source Serif 4", "Times New Roman", serif;
    font-size: 6.8px;
    line-height: 1.35;
    color: var(--white);
  }
  .back__ideas-title { font-weight: 700; font-size: 7.3px; }
</style>
</head>
<body>
  <div class="side-label side-label--front">FRONT</div>
  <div class="side-label side-label--back">BACK</div>

  <section class="card card--front">
    <div class="front__est">EST 2015</div>
    <div class="front__brand">Norrel Glow Co</div>
    <div class="front__feather" role="img" aria-label="Feather illustration"></div>
    <div class="front__tagline">Handmade on the Marrow Coast</div>
    <div class="front__region">KS, AUSTRALIA</div>
  </section>

  <section class="card card--back">
    <div class="back__name">Jess Pendell</div>

    <div class="contact contact--location">
      <svg viewBox="0 0 20 20" aria-hidden="true"><path d="M10 2 1 10h2.5v8h5v-5h3v5h5v-8H19z"/></svg>
      <span>Marrow Coast, KS Australia</span>
    </div>
    <div class="contact contact--phone">
      <svg viewBox="0 0 20 20" aria-hidden="true"><path d="M5.5 2 8 6.5 6.3 8.2c1 2.2 3.2 4.4 5.5 5.5L13.5 12 18 14.5 16.7 18C9 18 2 11 2 3.3z"/></svg>
      <span>0481 276 152.</span>
    </div>
    <div class="contact contact--email">
      <svg viewBox="0 0 20 20" aria-hidden="true"><path d="M1 4h18v1.5L10 11 1 5.5zM1 7.5l9 5.5 9-5.5V16H1z"/></svg>
      <span>norrelglowco@mailbrook.com.au</span>
    </div>
    <div class="contact contact--web">
      <svg viewBox="0 0 20 20" aria-hidden="true"><g fill="none" stroke="#fff" stroke-width="1.4"><circle cx="10" cy="10" r="8.3"/><ellipse cx="10" cy="10" rx="3.6" ry="8.3"/><path d="M1.7 10h16.6M3 5.8h14M3 14.2h14"/></g></svg>
      <span>craftmarketa.com/au/shop/NorrelGlowCo</span>
    </div>

    <div class="back__invite">
      We would love to see how you display your candle or reuse the glass vessel and would love to see a photo!<br>
      Check out ideas and share yours on your social media <strong>#norrelglowco</strong>
    </div>

    <div class="back__ideas">
      <div class="back__ideas-title">Just a few ideas to reuse your vessel;</div>
      <div>• A Vase to Display fresh flowers &nbsp; •Lolly Jar for your favourite candy</div>
      <div>•Decorate with baubles at Christmas &nbsp;•Bathroom Vanity Storage &nbsp;• Decorate with eggs at Easter</div>
    </div>
  </section>
</body>
</html>
```